One of Australia's fastest growing Financial Company looking for an updated business card design!

Meridale Partners Australia is looking for an updated design for our business cards. We would like to keep up our professional appearances and have get new exciting design that fits our company.

The Meridale aim is to facilitate and assist clients in every financial requirement that may arise in financial areas.

We would to see the design to use colour blue and we like the clouds in the background. We have attached two designs we have use before but we need something with more professional and easy to read design.

We would like the website in the back of the card; the employees name more central and stands out; only a postal address; a list of all our locations along the bottom (Sydney, Melbourne, Brisbane, Singapore)

Looking forward to seeing the designs come in!

Target Market(s)

Other Industry Professionals
Middle Class Families

Industry/Entity Type

Finance

Contact Information for Business Card

Name; Company Role; Office Number; Mobile Number; Email Address; Website; Postal Address; Locations

Font styles to use
Serif
Sans Serif

Colors
0492cd
33a6d7
85cae6
85acd3
3176b5
0455a3
cee9f5
d5e2ee

Requirements
Must have
• Name; Company Role; Office Number; Mobile Number; Email Address; Website; Postal Address; Locations
Nice to have
• The colour blue, clouds on the background

```html
<!DOCTYPE html>
<html lang="en">
<head>
<meta charset="utf-8">
<title>Meridale Business Card</title>
<link href="https://fonts.googleapis.com/css2?family=Montserrat:wght@400;500;700;800&display=swap" rel="stylesheet">
<style>
  :root {
    --brand-red: #ee3a3f;
    --brand-blue: #1a8fd6;
    --deep-blue: #0b6fb8;
    --card-white: #ffffff;
    --backdrop: #e9edf1;
    --ink-light: #3a9bd8;
  }
  * { margin: 0; padding: 0; box-sizing: border-box; }
  html, body { width: 1200px; height: 900px; overflow: hidden; }
  body {
    background: var(--backdrop);
    font-family: "Montserrat", Arial, sans-serif;
    position: relative;
  }
  .card {
    position: absolute;
    width: 600px;
    height: 343px;
    border-radius: 22px;
    box-shadow: 0 10px 30px rgba(0,0,0,0.18);
    overflow: hidden;
  }
  /* Front */
  .card-front {
    left: 80px; top: 90px;
    background: var(--brand-red);
  }
  .front-mark {
    position: absolute;
    left: 0; right: 0; top: 130px;
    display: flex; align-items: center; justify-content: center; gap: 18px;
  }
  .front-mark .dot {
    width: 44px; height: 44px; border-radius: 50%;
    background: var(--card-white);
  }
  .front-mark .name {
    color: var(--card-white);
    font-weight: 800;
    font-size: 68px;
    letter-spacing: 1px;
  }
  .front-web {
    position: absolute;
    right: 26px; bottom: 22px;
    color: var(--card-white);
    font-size: 15px;
    letter-spacing: 0.5px;
  }
  .front-web b { font-weight: 800; }

  /* Back */
  .card-back {
    left: 520px; top: 470px;
    background: var(--card-white);
  }
  .back-mark {
    position: absolute;
    left: 30px; top: 36px;
    display: flex; align-items: center; gap: 12px;
  }
  .back-mark .dot {
    width: 30px; height: 30px; border-radius: 50%;
    background: var(--brand-red);
  }
  .back-mark .name {
    color: var(--brand-blue);
    font-weight: 700;
    font-size: 56px;
    letter-spacing: 0.5px;
  }
  .holder {
    position: absolute;
    right: 28px; top: 132px;
    text-align: right;
  }
  .holder-name {
    color: var(--brand-red);
    font-weight: 800;
    font-size: 22px;
    letter-spacing: 1.5px;
  }
  .holder-role {
    color: var(--ink-light);
    font-size: 14px;
    letter-spacing: 1.5px;
    margin-top: 2px;
  }
  .divider {
    position: absolute;
    left: 30px; right: 28px; top: 196px;
    height: 2px; background: var(--brand-red);
  }
  .contact-list {
    position: absolute;
    right: 28px; top: 210px;
    list-style: none;
    text-align: right;
    color: var(--deep-blue);
    font-size: 15px;
    line-height: 1.45;
  }
  .contact-list li { display: flex; justify-content: flex-end; align-items: center; gap: 8px; }
  .contact-list svg { width: 12px; height: 12px; fill: var(--brand-red); }
  .locations {
    position: absolute;
    left: 30px; top: 222px;
    color: var(--deep-blue);
    font-weight: 800;
    font-size: 15px;
    letter-spacing: 1px;
    line-height: 1.3;
  }
  .locations-rule {
    position: absolute;
    left: 30px; top: 272px;
    width: 200px; height: 2px;
    background: var(--brand-red);
  }
  .postal {
    position: absolute;
    left: 30px; bottom: 22px;
    color: var(--brand-red);
    font-size: 14px;
    letter-spacing: 1px;
    opacity: 0.85;
  }
</style>
</head>
<body>
  <section class="card card-front">
    <div class="front-mark">
      <span class="dot"></span>
      <span class="name">Meridale</span>
    </div>
    <p class="front-web">www.<b>meridale</b>.com</p>
  </section>

  <section class="card card-back">
    <div class="back-mark">
      <span class="dot"></span>
      <span class="name">Meridale</span>
    </div>

    <div class="holder">
      <p class="holder-name">ARON WHITLEY</p>
      <p class="holder-role">DIRECTOR</p>
    </div>

    <div class="divider"></div>

    <ul class="contact-list">
      <li>555-214-3380
        <svg viewBox="0 0 24 24"><path d="M3 8c0-3 4-4 9-4s9 1 9 4v2h-5V8H8v2H3zM6 12h12l2 8H4z"/></svg></li>
      <li>555-214-3391
        <svg viewBox="0 0 24 24"><path d="M6 2l4 4-2 3c1 3 4 6 7 7l3-2 4 4-3 4C10 22 2 14 2 5z"/></svg></li>
      <li>info@meridale.com
        <svg viewBox="0 0 24 24"><path d="M2 5h20v14H2zm2 2v1l8 5 8-5V7l-8 5z"/></svg></li>
      <li>www.meridale.com
        <svg viewBox="0 0 24 24"><circle cx="12" cy="12" r="10"/></svg></li>
    </ul>

    <p class="locations">SYDNEY, MELBOURNE,<br>BRISBANE, SINGAPORE</p>
    <div class="locations-rule"></div>
    <p class="postal">PO Box 4127</p>
  </section>
</body>
</html>
```